More Modern Look Required! Industry leading Property Management company needs a new website!

We are wanting to make our website more modern, as we find it is too cluttered, seems "old" and we want a new look. (www.tallowbrookrm.com)

We are wanting something fresh, clean and responsive, something that aligns with today's social media demands, something that allows our potential customers to immediately get a sense of the type of company we are.

Our current website was created on Wordpress and we will be keeping that core platform but wanting a new look and feel to it. The only thing we want to keep on the website is our "FOR RENT" page, although again we are open to having that look completely different as well (our programmers can adapt the functionality later)

Here is a synopsis of our branding statements:

CORE VALUES:
1. Passion
2. Innovation
3. Integrity (doing the right thing, even when it's difficult)
4. Empathy
5. Education

CORE FOCUS:
Our vision is to be the premier company for the delivery of all aspects of property management showing our passion for this industry, by innovating our service using cutting-edge technology, helping and educating investors to create aspirational and sustainable communities, adding value to their real estate assets, and working in partnership with all stakeholders including residents, showing empathy and integrity.

Brand Essence

When our customers experience our product or service, it brings forth an emotion of absolute trust that we have their best interests at heart

Brand Personality

We are a company that is passionate about our customers, our company and our vision to be leaders in the field of property management. We are visionaries that aren't afraid to use cutting edge technologies to improve our products and service.

Position or Value Proposition

To whom are we speaking?
- real estate investors, including first timers that are giving us their first starter home. They are not "big time" investors, and because they are giving us their first home (in contrast to an investor buying a rental property, often sight unseen) they are more emotionally tied to their property and will require a company that inspires trust and confidence.

What is our brand promise?
- we will do our best to serve our clients, both owners and tenants, to give them prompt communication, clear, concise answers to their questions, and look after their property quickly and competently.

Why is our product different than the competition and why should our customers care?
- Our management product is superior because we use a combination of technology and strict procedures to ensure each client's experience is consistent, each and every time.
Updates

Need extra days to review

Industry/Entity Type

Real Estate and Property Management

Number of Pages Required

5+ page

Requirements
Must have
• Must be compatible on Wordpress, our existing web platform. Please see our existing website at www.tallowbrookrm.com to familiarize yourself with our current site. Must incorporate For Rent section
Nice to have
• Built in reviews, contact us form, awards page including Fernleigh Patron Prizes (we just won again for Best Property Management Company, 8 years in a row)
Should not have
• Too many pages. Currently we feel there is too much information on each tab, and we can consolidate into about 5 or 6 tabs.

```html
<!DOCTYPE html>
<html lang="en">
<head>
<meta charset="utf-8">
<title>Property Management Pricing – Tallowbrook Property Management</title>
<link rel="stylesheet" href="https://fonts.googleapis.com/css2?family=Figtree:wght@400;500;600;700&family=Open+Sans:ital,wght@0,400;0,600;0,700;1,400&display=swap">
<style>
:root{
  --ink:#141414;
  --text:#333;
  --muted:#666;
  --blue:#1e90d2;
  --blue-dark:#1577b6;
  --blue-deep:#0d4f98;
  --sky:#8ed6f8;
  --line:#d9d9d9;
  --head-grey:#e4e4e4;
  --white:#fff;
  --pale:#e9f4fb;
}
*{box-sizing:border-box;margin:0;padding:0}
html,body{width:1200px;height:3785px;overflow:hidden}
body{position:relative;background:var(--white);font-family:"Open Sans",sans-serif;color:var(--text)}
.abs{position:absolute}

/* top bar */
.topbar{left:0;top:0;width:1200px;height:59px;background:var(--ink)}
.brand{display:flex;align-items:center;gap:10px;color:var(--blue);font-family:"Figtree",sans-serif;font-weight:700;text-transform:uppercase;line-height:1.05;letter-spacing:1px}
.brand .mark{width:34px;height:34px;background:var(--blue)}
.topbar .brand{left:62px;top:9px;font-size:17px}
.topbar .brand small{display:block;font-size:10px;letter-spacing:3px}
.contacts{right:70px;top:20px;display:flex;align-items:center;gap:16px;color:var(--white);font-family:"Figtree",sans-serif;font-weight:700;font-size:11px}
.contacts span{display:flex;align-items:center;gap:6px}
.contacts .btn{background:var(--blue);padding:4px 9px;text-transform:uppercase}

/* nav */
.nav{left:0;top:59px;width:1200px;height:40px;background:var(--blue);display:flex;font-family:"Figtree",sans-serif;font-weight:600;font-size:11px;color:var(--white);text-transform:uppercase}
.nav a{display:flex;align-items:center;justify-content:center;text-decoration:none;color:inherit;height:100%}
.nav .active{background:var(--blue-dark);color:#bfe6ff}

/* hero */
.hero{left:0;top:99px;width:1200px;height:592px;background:linear-gradient(180deg,#5cc3f3 0%,var(--sky) 55%,#b4e6fb 100%)}
.hero-curve{left:0;top:520px;width:1200px;height:172px}

/* headings */
.section-title{left:0;width:1200px;text-align:center;color:var(--blue);font-family:"Figtree",sans-serif;font-weight:600;text-transform:uppercase;letter-spacing:.5px}
.tagline{left:0;top:838px;width:1200px;text-align:center;color:var(--blue);font-family:"Figtree",sans-serif;font-weight:500;font-size:28px;line-height:36px}

/* comparison table */
.compare-head{left:470px;top:950px;width:526px;text-align:center}
.compare-head h3{color:var(--blue);font-family:"Figtree",sans-serif;font-weight:700;font-size:13px}
.compare-head p{font-size:8px;color:var(--muted);margin-top:5px}
.compare{left:204px;top:993px;width:792px;border-collapse:collapse;font-size:10px}
.compare td,.compare th{border:1px solid var(--line);vertical-align:middle}
.compare thead th{height:92px;background:var(--head-grey);font-weight:400;color:var(--ink);padding:4px 8px}
.compare thead th.blank{background:var(--white);border:none;border-right:1px solid var(--line);width:266px}
.compare thead th.popular{background:var(--blue);color:var(--white)}
.compare thead .plan{font-family:"Figtree",sans-serif;font-size:14px;line-height:16px}
.compare thead .tag{font-size:9px;text-transform:uppercase;display:block;margin-bottom:4px}
.compare thead .note{font-size:9px;display:block;margin-top:4px}
.compare .price-row td{height:88px;text-align:center;font-size:7px;line-height:13px;color:var(--text)}
.compare .price-row td.blank{border:none;border-right:1px solid var(--line);border-bottom:1px solid var(--line)}
.compare .price-row strong{display:block;font-family:"Figtree",sans-serif;font-size:16px;color:var(--blue);line-height:22px}
.compare .price-row strong em{font-style:normal;font-size:10px;font-weight:500}
.compare tbody tr{height:30px}
.compare tbody tr.tall{height:38px}
.compare tbody td:first-child{padding:2px 6px;color:var(--text);line-height:12px}
.compare tbody td.c{text-align:center}
.tick{width:20px;height:20px;vertical-align:middle}
.footnotes{left:204px;top:1814px;width:792px;text-align:center;font-size:8px;color:var(--muted);line-height:12px}
.footnotes p{margin-bottom:8px}

/* videos */
.subtitle{left:0;top:1998px;width:1200px;text-align:center;font-size:8px;color:var(--muted)}
.subtitle b{color:var(--blue)}
.video{top:2040px;width:238px;height:133px;background:linear-gradient(135deg,#6a6a63,#b9b3a4 55%,#4d4d4a)}
.video .label{position:absolute;left:14px;top:6px;font-family:"Figtree",sans-serif;font-weight:700;color:var(--white);font-size:9px;background:var(--ink);padding:2px 6px}
.video .controls{position:absolute;left:4px;right:4px;bottom:4px;height:16px;background:rgba(0,0,0,.75)}
.video .controls i{position:absolute;left:6px;top:4px;border-left:7px solid var(--white);border-top:4px solid transparent;border-bottom:4px solid transparent}
.video .controls b{position:absolute;left:22px;right:80px;top:7px;height:2px;background:#888}

/* homewatch grid */
.hw{left:209px;top:2286px;width:790px;color:var(--white);font-family:"Figtree",sans-serif}
.hw-row{display:flex;gap:3px;margin-bottom:3px}
.hw-cell{background:var(--blue);padding:10px}
.hw-name{width:195px;display:flex;align-items:center;font-size:12px;font-weight:600;line-height:17px}
.hw-price{width:192px;display:flex;flex-direction:column;align-items:center;justify-content:center;text-align:center;font-size:10px;line-height:12px}
.hw-price strong{font-size:29px;font-weight:700;line-height:40px}
.hw-list{flex:1;font-family:"Open Sans",sans-serif;font-size:9.5px;line-height:13.5px}
.hw-list u{display:block;margin-bottom:12px}
.hw-list ul{padding-left:16px}
.hw-extra .hw-cell{background:var(--pale);color:var(--blue);font-size:10px;display:flex;align-items:center;height:37px}
.hw-extra .leader{flex:1;height:1px;background:var(--blue);margin:0 4px}
.hw-incl{display:flex;background:var(--blue);padding:10px 0 10px 115px;font-family:"Open Sans",sans-serif;font-size:9.5px;line-height:13.5px;height:85px}
.hw-incl ul{padding-left:14px}
.hw-incl div{width:275px}

/* supplementary */
.supp-title{left:207px;top:2701px;color:var(--blue);font-family:"Figtree",sans-serif;font-weight:500;font-size:17px}
.supp{left:207px;width:792px;display:flex;align-items:center;font-size:10px;color:var(--ink);line-height:12px}
.supp .leader{flex:1;height:1px;background:#888;margin:0 8px;position:relative}
.supp .leader::before,.supp .leader::after{content:"";position:absolute;top:-1px;width:3px;height:3px;border-radius:50%;background:var(--ink)}
.supp .leader::before{left:0}.supp .leader::after{right:0}
.supp-note{left:207px;top:2981px;font-size:6px;font-style:italic;color:var(--ink)}

/* closing swoosh + footer */
.swoosh{left:0;top:3196px;width:1200px;height:490px}
.footer{left:0;top:3680px;width:1200px;height:105px;background:var(--ink);color:var(--white)}
.footer .brand{left:28px;top:26px;font-size:22px}
.footer .brand small{display:block;font-size:11px;letter-spacing:3.5px}
.footer .brand .mark{width:40px;height:40px}
.foot-nav{left:362px;top:36px;display:flex;gap:0;font-family:"Figtree",sans-serif;font-size:8.5px;font-weight:600;text-transform:uppercase}
.foot-nav span{width:66px;line-height:10px}
.foot-meta{left:282px;top:85px;font-size:7.5px;display:flex;gap:24px}
.social{left:1036px;top:36px;display:flex;gap:14px}
.social i{width:16px;height:16px;border-radius:50%;background:var(--white);display:block}
</style>
</head>
<body>
<svg width="0" height="0" style="position:absolute">
  <defs>
    <symbol id="tick" viewBox="0 0 24 24">
      <path d="M20.5 10.5A9 9 0 1 1 15.5 3.8" fill="none" stroke="#111" stroke-width="2.2" stroke-linecap="round"/>
      <path d="M7.5 11.5l4 4 9-10" fill="none" stroke="#111" stroke-width="2.4" stroke-linecap="round" stroke-linejoin="round"/>
    </symbol>
  </defs>
</svg>

<header class="abs topbar">
  <div class="abs brand"><span class="mark"></span><span>Tallowbrook<small>Property Management</small></span></div>
  <div class="abs contacts">
    <span><svg width="16" height="16" viewBox="0 0 24 24"><path d="M6.6 10.8a15 15 0 0 0 6.6 6.6l2.2-2.2c.3-.3.7-.4 1-.2 1.1.4 2.3.6 3.6.6.6 0 1 .4 1 1V20c0 .6-.4 1-1 1A17 17 0 0 1 3 4c0-.6.4-1 1-1h3.5c.6 0 1 .4 1 1 0 1.3.2 2.5.6 3.6.1.3 0 .7-.2 1z" fill="#1e90d2"/></svg>PH: 204-555-0142</span>
    <span><svg width="16" height="16" viewBox="0 0 24 24"><rect x="3" y="3" width="18" height="18" rx="2" fill="#1e90d2"/><path d="M8 8c0 5 3 8 8 8l1-2-2-1-1 1c-2-1-3-2-4-4l1-1-1-2z" fill="#fff"/></svg>TOLL FREE: 1-800-555-0199</span>
    <span class="btn">Login</span>
    <span class="btn">Create Maintenance Ticket</span>
  </div>
</header>

<nav class="abs nav">
  <a style="width:175px">Home</a>
  <a style="width:160px">Services ⌄</a>
  <a class="active" style="width:122px">Pricing ⌄</a>
  <a style="width:200px">Homewatch &amp; Leasing Only</a>
  <a style="width:112px">Rentals</a>
  <a style="width:210px">About Us ⌄</a>
  <a style="width:221px">Contact Us ⌄</a>
</nav>

<div class="abs hero" role="img" aria-label="Illustration of a small orange house with a blue roof between stacks of copper coins"></div>
<svg class="abs hero-curve" viewBox="0 0 1200 172" preserveAspectRatio="none"><path d="M0 25 Q600 340 1200 25 V172 H0 Z" fill="#fff"/></svg>

<h1 class="abs section-title" style="top:720px;font-size:30px">Property Management Pricing</h1>
<svg class="abs" style="left:584px;top:792px" width="32" height="36" viewBox="0 0 32 36"><path d="M5 4h17a4 4 0 0 1 0 8h-3v4a6 6 0 0 1-6 6v8a3 3 0 0 1-6 0v-8a6 6 0 0 1-6-6V7a3 3 0 0 1 4-3z" fill="none" stroke="#1e90d2" stroke-width="3" stroke-linejoin="round"/></svg>
<p class="abs tagline">Our Company Cares about responsible growth!<br>Choose an appointment time that works for you.</p>

<div class="abs compare-head"><h3>TALLOWBROOK PRICING</h3><p>Complete transparency. No locked in contracts *</p></div>
<table class="abs compare">
  <thead>
    <tr>
      <th class="blank"></th>
      <th style="width:166px"><span class="plan">"No More Midnight Phone Calls"</span><span class="note">(Property Maintenance)</span></th>
      <th class="popular" style="width:172px"><span class="tag">Most Popular</span><span class="plan">"Full Service Management"</span><span class="note">(Maintenance plus full Tenant Management)</span></th>
      <th style="width:188px"><span class="plan">"Peace of Mind"</span><span class="note">(Full service management plus Court Protection)</span></th>
    </tr>
  </thead>
  <tbody>
    <tr class="price-row">
      <td class="blank"></td>
      <td><strong>$70 <em>per month</em></strong>$70 Monthly Admin Fee +<br>$29 Maintenance Coordination Fee<br>*Total $99</td>
      <td><strong>$175 <em>per month</em></strong>$175 Monthly Management Fee** +<br>$29 Maintenance Coordination Fee<br>*Total $204</td>
      <td><strong>$195 <em>per month</em></strong>$175 Monthly Management Fee** +<br>$29 Maintenance Coordination Fee +<br>$20 Court Protection Package ***<br>*Total $224</td>
    </tr>
    <tr><td>24/7 emergency call centre and dispatch</td><td class="c"><svg class="tick"><use href="#tick"/></svg></td><td class="c"><svg class="tick"><use href="#tick"/></svg></td><td class="c"><svg class="tick"><use href="#tick"/></svg></td></tr>
    <tr><td>Tenant can create online maintenance tickets</td><td class="c"><svg class="tick"><use href="#tick"/></svg></td><td class="c"><svg class="tick"><use href="#tick"/></svg></td><td class="c"><svg class="tick"><use href="#tick"/></svg></td></tr>
    <tr><td>Automatic maintenance owner notifications</td><td class="c"><svg class="tick"><use href="#tick"/></svg></td><td class="c"><svg class="tick"><use href="#tick"/></svg></td><td class="c"><svg class="tick"><use href="#tick"/></svg></td></tr>
    <tr class="tall"><td>Owner asked for permission before proceeding (except emergencies)</td><td class="c"><svg class="tick"><use href="#tick"/></svg></td><td class="c"><svg class="tick"><use href="#tick"/></svg></td><td class="c"><svg class="tick"><use href="#tick"/></svg></td></tr>
    <tr><td>Chat interface for all parties to communicate</td><td class="c"><svg class="tick"><use href="#tick"/></svg></td><td class="c"><svg class="tick"><use href="#tick"/></svg></td><td class="c"><svg class="tick"><use href="#tick"/></svg></td></tr>
    <tr class="tall"><td>Customer service survey sent to every tenant after completion of job</td><td class="c"><svg class="tick"><use href="#tick"/></svg></td><td class="c"><svg class="tick"><use href="#tick"/></svg></td><td class="c"><svg class="tick"><use href="#tick"/></svg></td></tr>
    <tr class="tall"><td>Actual contractor invoices uploaded into online owner portal</td><td class="c"><svg class="tick"><use href="#tick"/></svg></td><td class="c"><svg class="tick"><use href="#tick"/></svg></td><td class="c"><svg class="tick"><use href="#tick"/></svg></td></tr>
    <tr class="tall"><td>Access to investor For Sale property listings (no commissions)</td><td class="c"><svg class="tick"><use href="#tick"/></svg></td><td class="c"><svg class="tick"><use href="#tick"/></svg></td><td class="c"><svg class="tick"><use href="#tick"/></svg></td></tr>
    <tr><td>Accounting and reporting</td><td class="c"><svg class="tick"><use href="#tick"/></svg></td><td class="c"><svg class="tick"><use href="#tick"/></svg></td><td class="c"><svg class="tick"><use href="#tick"/></svg></td></tr>
    <tr><td>Owner anonymity</td><td></td><td class="c"><svg class="tick"><use href="#tick"/></svg></td><td class="c"><svg class="tick"><use href="#tick"/></svg></td></tr>
    <tr><td>Portfolio management</td><td></td><td class="c"><svg class="tick"><use href="#tick"/></svg></td><td class="c"><svg class="tick"><use href="#tick"/></svg></td></tr>
    <tr><td>Tenant management</td><td></td><td class="c"><svg class="tick"><use href="#tick"/></svg></td><td class="c"><svg class="tick"><use href="#tick"/></svg></td></tr>
    <tr><td>Rent collection</td><td></td><td class="c"><svg class="tick"><use href="#tick"/></svg></td><td class="c"><svg class="tick"><use href="#tick"/></svg></td></tr>
    <tr class="tall"><td>Warning letters, follow-up inspections, contractual disputes</td><td></td><td class="c"><svg class="tick"><use href="#tick"/></svg></td><td class="c"><svg class="tick"><use href="#tick"/></svg></td></tr>
    <tr><td>Meter readings</td><td></td><td class="c"><svg class="tick"><use href="#tick"/></svg></td><td class="c"><svg class="tick"><use href="#tick"/></svg></td></tr>
    <tr><td>Lease management</td><td></td><td class="c"><svg class="tick"><use href="#tick"/></svg></td><td class="c"><svg class="tick"><use href="#tick"/></svg></td></tr>
    <tr><td>Accounting and reporting</td><td></td><td class="c"><svg class="tick"><use href="#tick"/></svg></td><td class="c"><svg class="tick"><use href="#tick"/></svg></td></tr>
    <tr class="tall"><td>Eligible for Group Insurance Plan (~45% discount off retail)</td><td></td><td class="c"><svg class="tick"><use href="#tick"/></svg></td><td class="c"><svg class="tick"><use href="#tick"/></svg></td></tr>
    <tr><td>Court protection ***</td><td></td><td></td><td class="c"><svg class="tick"><use href="#tick"/></svg></td></tr>
  </tbody>
</table>

<div class="abs footnotes">
  <p>* Management contracts have no term. If you find we are not a good fit for you, stop anytime.</p>
  <p>** Our fees are charged out at a flat rate. $175 is the maximum price for a single family home. Discounts are given for multiple units in the same building (i.e $154.4 per unit for a duplex) and investors with multiple houses qualify for further discounts (eg: investor with 5 houses pay $155 per house, per month). Management fees are NOT charged if the unit is vacant.</p>
  <p>*** Court protection includes all costs if it is necessary to take the tenant to court over unpaid rent or an eviction for noise complaints, etc. Typical court costs are approximately $650 or more.</p>
</div>

<h2 class="abs section-title" style="top:1960px;font-size:31px">Choosing a Plan</h2>
<p class="abs subtitle">Which plan is right for you? <b>CLICK HERE</b> to request our full pricing brochure.</p>
<div class="abs video" style="left:207px" role="img" aria-label="Video: Full Service Plan presentation in an office"><span class="label">Full Service Plan</span><span class="controls"><i></i><b></b></span></div>
<div class="abs video" style="left:480px" role="img" aria-label="Video: Full Service Plan presentation in an office"><span class="label">Full Service Plan</span><span class="controls"><i></i><b></b></span></div>
<div class="abs video" style="left:752px" role="img" aria-label="Video: Full Service Plan presentation in an office"><span class="label">Full Service Plan</span><span class="controls"><i></i><b></b></span></div>

<h2 class="abs section-title" style="top:2230px;font-size:31px">Property Management Pricing</h2>
<section class="abs hw">
  <div class="hw-row" style="height:114px">
    <div class="hw-cell hw-name">Standard<br>Homewatch<br>Service</div>
    <div class="hw-cell hw-price"><strong>$96.00</strong>per month<br>(incl. 4 visits)</div>
    <div class="hw-cell hw-list"><u>Ensuring:</u><ul><li>Property secure</li><li>No water leaks</li><li>Heat operational, including photo of thermostat</li></ul></div>
  </div>
  <div class="hw-row" style="height:156px">
    <div class="hw-cell hw-name">Enhanced<br>Homewatch<br>Service</div>
    <div class="hw-cell hw-price"><strong>$125.00</strong>per month<br>(incl. 4 visits)</div>
    <div class="hw-cell hw-list"><u>Ensuring:</u><ul><li>Property secure</li><li>No water leaks</li><li>Heat operational, including photo of thermostat<br>plus:</li><li>Perimeter inspection for break-ins</li><li>Collect mail, take inside</li><li>Walk through each room, including basement</li><li>Customized tasks upon request *</li></ul></div>
  </div>
  <div class="hw-row hw-extra">
    <div class="hw-cell" style="width:195px;font-size:12px;font-weight:600">Additional Visits:</div>
    <div class="hw-cell" style="width:192px">Standard<span class="leader"></span>$19.50</div>
    <div class="hw-cell" style="flex:1">Enhanced<span class="leader"></span>$25.50</div>
  </div>
  <div class="hw-incl">
    <div><u>All packages include:</u><ul style="margin-top:12px"><li>Scheduling of all inspections</li><li>Online access to view reports/photos</li><li>Dispatch of emergency maintenance personnel</li></ul></div>
    <div style="padding-top:14px"><ul><li>Open &amp; maintain trust account ledger, payment of any invoices</li><li>Monthly reporting &amp; accounting statements</li><li>Coordination with owner for any other maintenance</li></ul></div>
  </div>
</section>

<h3 class="abs supp-title">Supplementary Services</h3>
<div class="abs supp" style="top:2734px"><span>Weekly Grass Cutting</span><span class="leader"></span><span>$ price per cut (ask for quote)</span></div>
<div class="abs supp" style="top:2784px"><span>Snow removal</span><span class="leader"></span><span>$ price per week (ask for quote)</span></div>
<div class="abs supp" style="top:2835px"><span>Fall eavestrough cleaning</span><span class="leader"></span><span>ask for quote</span></div>
<div class="abs supp" style="top:2866px"><span style="width:240px">Annual furnace cleaning (includes changing basic furnace filter, thermostat batteries)</span><span class="leader"></span><span>ask for quote</span></div>
<div class="abs supp" style="top:2903px"><span style="width:150px">Housekeeping services (prior to returning from vacation, etc)</span><span class="leader"></span><span>ask for quote</span></div>
<div class="abs supp" style="top:2950px"><span style="width:120px">Grocery pickup and restocking fridge</span><span class="leader"></span><span>ask for quote</span></div>
<p class="abs supp-note">* If owner would like special items inspected/verified, this can be arranged, time permitting. Time intensive tasks are also possible, but may be subject to extra fees. Please discuss this with your representative</p>

<svg class="abs swoosh" viewBox="0 0 1200 490" preserveAspectRatio="none">
  <defs>
    <linearGradient id="sw" x1="0" y1="0" x2="1" y2="1"><stop offset="0" stop-color="#2a9ee0"/><stop offset="1" stop-color="#0b3f8a"/></linearGradient>
  </defs>
  <path d="M0 290 C350 410 800 360 1200 0 V490 H0 Z" fill="url(#sw)"/>
  <path d="M0 340 C400 450 850 380 1200 100 V490 H0 Z" fill="#1a6dbc" opacity=".55"/>
  <path d="M0 310 C380 420 840 370 1200 40" fill="none" stroke="#cfe9fb" stroke-width="6" opacity=".8"/>
  <path d="M0 390 C420 470 880 400 1200 160 V490 H0 Z" fill="#0d4f98"/>
</svg>

<footer class="abs footer">
  <div class="abs brand"><span class="mark"></span><span>Tallowbrook<small>Property Management</small></span></div>
  <div class="abs foot-nav"><span>Home</span><span>Services</span><span>Pricing</span><span>Homewatch &amp;<br>Leasing Only</span><span>About Us</span><span>Rentals</span><span>Contact Us</span></div>
  <div class="abs foot-meta"><span>© 2023 TALLOWBROOK PROPERTY MANAGEMENT. ALL RIGHT RESERVED.</span><span>PH: 204-555-0142</span><span>TOLL FREE: 1-800-555-0199</span><span>INFO@TALLOWBROOKRM.COM</span></div>
  <div class="abs social"><i></i><i></i><i></i><i></i></div>
</footer>
</body>
</html>
```